Bright Oak Fitness Facility Business Cards

Business Card Design that incorporates the logo and tagline

Target Market(s)

Fitness, People Who Exercise

Contact Information for Business Card

2817 Mossgrove Bend Road
Maple Hollow, Ohio 43990
Phone: 555-014-Jump (5867)
www.brightoakfitness.example
info@brightoakfitness.example

Requirements
Must have
• Logo, Address, Website, email and tagline "Stronger Every Day". Colors should be red/black/grey/white

```html
<!DOCTYPE html>
<html lang="en">
<head>
<meta charset="utf-8">
<title>Bright Oak Fitness Facility – Business Card</title>
<link rel="stylesheet" href="https://fonts.googleapis.com/css2?family=Open+Sans:wght@400;600;700&display=swap">
<style>
  :root {
    --brand-red: #e4262a;
    --ink: #1b1b1b;
    --paper: #ffffff;
    --backdrop: #2a2c2f;
    --grey: #8a8a8a;
  }
  * { box-sizing: border-box; margin: 0; padding: 0; }
  html, body {
    width: 1200px;
    height: 900px;
    overflow: hidden;
  }
  body {
    background: var(--backdrop);
    display: flex;
    align-items: center;
    justify-content: center;
    font-family: "Open Sans", Arial, sans-serif;
  }
  .business-card {
    width: 460px;
    height: 780px;
    background: var(--paper);
    border: 10px solid var(--brand-red);
    border-radius: 40px;
    display: flex;
    flex-direction: column;
    align-items: center;
    padding: 80px 30px 60px;
    text-align: center;
  }
  .brand {
    display: flex;
    align-items: center;
    justify-content: center;
    gap: 10px;
    margin-bottom: 10px;
    white-space: nowrap;
  }
  .brand-dot {
    flex: none;
    width: 20px;
    height: 20px;
    border-radius: 50%;
    background: var(--brand-red);
  }
  .brand-name {
    font-size: 30px;
    font-weight: 700;
    color: var(--ink);
    line-height: 1.1;
  }
  .brand-rule {
    width: 320px;
    height: 2px;
    background: var(--grey);
    margin-bottom: 24px;
  }
  .tagline {
    font-size: 30px;
    font-weight: 400;
    color: var(--ink);
    white-space: nowrap;
    margin-bottom: 60px;
  }
  .tagline .quote { color: var(--brand-red); }
  .contact-icons {
    display: flex;
    gap: 34px;
    align-items: center;
    margin-bottom: 30px;
  }
  .contact-icons svg { display: block; }
  .contact-lines {
    display: flex;
    flex-direction: column;
    gap: 6px;
    font-size: 22px;
    white-space: nowrap;
    margin-bottom: 70px;
  }
  .contact-phone, .contact-email { color: var(--brand-red); }
  .contact-web { color: var(--ink); }
  .address {
    font-size: 26px;
    font-style: normal;
    color: var(--ink);
    line-height: 1.4;
    white-space: nowrap;
  }
</style>
</head>
<body>
  <article class="business-card">
    <div class="brand">
      <span class="brand-dot"></span>
      <span class="brand-name">BRIGHT OAK FITNESS</span>
    </div>
    <div class="brand-rule"></div>

    <p class="tagline"><span class="quote">"</span>Stronger Every Day<span class="quote">"</span></p>

    <div class="contact-icons">
      <svg class="icon-phone" width="34" height="34" viewBox="0 0 34 34" aria-hidden="true">
        <path d="M9 6 L14 11 L11 15 Q14 21 19 23 L23 20 L28 25 L24 29 Q12 28 5 12 Z" fill="var(--brand-red)"/>
      </svg>
      <svg class="icon-globe" width="34" height="34" viewBox="0 0 34 34" aria-hidden="true">
        <circle cx="17" cy="17" r="15" fill="var(--ink)"/>
        <ellipse cx="17" cy="17" rx="6" ry="15" fill="none" stroke="#fff" stroke-width="1.5"/>
        <line x1="2" y1="17" x2="32" y2="17" stroke="#fff" stroke-width="1.5"/>
        <line x1="5" y1="10" x2="29" y2="10" stroke="#fff" stroke-width="1.2"/>
        <line x1="5" y1="24" x2="29" y2="24" stroke="#fff" stroke-width="1.2"/>
      </svg>
      <svg class="icon-mail" width="42" height="32" viewBox="0 0 42 32" aria-hidden="true">
        <rect x="2" y="2" width="38" height="28" fill="none" stroke="var(--brand-red)" stroke-width="3"/>
        <polyline points="2,2 21,18 40,2" fill="none" stroke="var(--brand-red)" stroke-width="3"/>
      </svg>
    </div>

    <div class="contact-lines">
      <span class="contact-phone">555-014-Jump (5867)</span>
      <span class="contact-web">www.brightoakfitness.example</span>
      <span class="contact-email">info@brightoakfitness.example</span>
    </div>

    <address class="address">
      2817 Mossgrove Bend Road<br>
      Maple Hollow, Ohio 43990
    </address>
  </article>
</body>
</html>
```